sydney wedding photography business needs a business card design

we need a business card design for a sydney based wedding photography and videography business. our business name is :golden hour studios and film. our target clients are 24-35 yrs female. our style is candid, organic, natural, dynamic. we are a team of young photographers and videographers, and help brides to create memories that they will cherish for the rest of their lives. the logo will be provided. we want an elegant design that reflects our style, and also want to give a great impression to our clients that we are one of the best studios in sydney and our brand means quality and premium service.

Target Market(s)

bride to be, 24-35 years old, living in sydney and surrunding areas

Industry/Entity Type

Wedding Photography

Contact Information for Business Card

address: 47 marrowbank street, lilyfield nsw 2040
mobile: 0417283951
phone: (02) 9163 2748
info@goldenhourstudio.net.au
www.goldenhourstudio.net.au
facebook:goldenhourbridals
instagram:goldenhourbridals

Font styles to use
Serif
Sans Serif

Requirements
Nice to have
• maybe add my slogan"memories beyond eternity" if the layout looks good
Should not have
• no black color, not good idea for wedding biz card

```html
<!DOCTYPE html>
<html lang="en">
<head>
<meta charset="utf-8">
<title>Golden Hour Studios – Business Card</title>
<link href="https://fonts.googleapis.com/css2?family=Cormorant+Garamond:ital,wght@0,500;1,500&display=swap" rel="stylesheet">
<style>
  :root {
    --backdrop: #5b3726;
    --card: #f3f3f3;
    --gold: #c99a1c;
    --gold-deep: #b8860f;
    --shadow: rgba(30, 15, 5, 0.45);
  }
  * { box-sizing: border-box; margin: 0; padding: 0; }
  html, body {
    width: 1200px;
    height: 864px;
    overflow: hidden;
    background: var(--backdrop);
  }
  .canvas {
    width: 1200px;
    height: 864px;
    display: flex;
    align-items: center;
    justify-content: center;
    gap: 56px;
  }
  .card {
    position: relative;
    width: 540px;
    height: 309px;
    background: var(--card);
    box-shadow: 0 14px 30px var(--shadow);
    font-family: "Cormorant Garamond", Georgia, serif;
    color: var(--gold);
  }
  /* Front */
  .card--front {
    display: flex;
    align-items: center;
    justify-content: center;
  }
  .brand-name {
    font-size: 46px;
    font-weight: 500;
    letter-spacing: 1px;
    color: var(--gold);
  }
  /* Back */
  .holder {
    position: absolute;
    left: 40px;
    top: 34px;
  }
  .holder__name {
    font-size: 34px;
    font-weight: 500;
    line-height: 1;
    color: var(--gold-deep);
  }
  .holder__role {
    font-size: 19px;
    font-style: italic;
    font-weight: 500;
    margin-top: 2px;
    color: var(--gold-deep);
  }
  .contacts {
    position: absolute;
    left: 40px;
    top: 128px;
    list-style: none;
    font-size: 17px;
    font-weight: 500;
    line-height: 1.45;
    color: var(--gold-deep);
  }
  .contacts li {
    display: flex;
    align-items: center;
    gap: 10px;
  }
  .contacts svg {
    width: 11px;
    height: 11px;
    flex: none;
  }
  .brand-mark {
    position: absolute;
    right: 36px;
    bottom: 30px;
    font-size: 22px;
    font-weight: 500;
    color: var(--gold);
  }
</style>
</head>
<body>
<main class="canvas">
  <section class="card card--front" aria-label="Card front">
    <h1 class="brand-name">Golden Hour Studios</h1>
  </section>

  <section class="card card--back" aria-label="Card back">
    <div class="holder">
      <p class="holder__name">Lena Marsh</p>
      <p class="holder__role">Photography</p>
    </div>
    <ul class="contacts">
      <li>
        <svg viewBox="0 0 12 12" aria-hidden="true"><rect x="2.5" y="1" width="7" height="10" rx="1.2" fill="none" stroke="currentColor" stroke-width="1.4"/></svg>
        0417 283 951
      </li>
      <li>
        <svg viewBox="0 0 12 12" aria-hidden="true"><rect x="1" y="2.5" width="10" height="7" fill="none" stroke="currentColor" stroke-width="1.3"/><path d="M1 3l5 4 5-4" fill="none" stroke="currentColor" stroke-width="1.3"/></svg>
        info@goldenhourstudio.net.au
      </li>
      <li>
        <svg viewBox="0 0 12 12" aria-hidden="true"><circle cx="6" cy="6" r="5" fill="none" stroke="currentColor" stroke-width="1.3"/><path d="M1 6h10M6 1c-2.5 3-2.5 7 0 10M6 1c2.5 3 2.5 7 0 10" fill="none" stroke="currentColor" stroke-width="1"/></svg>
        www.goldenhourstudio.net.au
      </li>
    </ul>
    <p class="brand-mark">Golden Hour Studios</p>
  </section>
</main>
</body>
</html>
```